Mediakit / brochure for Dutch Travel Blog

About our company:
• Bolderwijk.nl is a Travel- & influence network for independent travellers, outdoor geeks, culture lovers & adventure seekers.
• We don’t sell trips by ourself, we inspire other to travel.
• It’s all about travel inspiration.

About the media kit / brochure:
• The media kit itself must be a travel experience / inspiration.
• Colourful and clean design.
• Use the colours of our new logo
• Use our icons (marker, worldmap) in the design
• Use the style of our website.
• All the text in the media kit must be adjustable by us
• Page format: A4
• Number of pages: 6
• It must be printable as a brochure (for presentations)
• We also need a .pdf version of the brochure (for emailing it to our partners)
• Logo kit added: (1a) + (1b) + (1c) Logo sourcefile

Content of the media kit / brochure
• 6 pages
o (1) Front page
o (2) About Us
o (3) Stats / Companies work with
o (4) Advertising
o (5) Back page
o (6) Our contributors

• Example is attached: (2) example of a brochure with 5 pages A4 (don’t like the design of this example for our media kit, but just to show the idea of the 5 pages).

Maybe use a big travel photo that covers all pages?

For detailed information, I attached the document 'Design brochure Bolderwijk (version 2)'.
Updates

Hello designers,Small update for the Cover Page:- Please use one of the images from the attachment I added in the Brief Design: "URL of images for cover.txt"- Use this text "Travel- & influence network for independent travelers, outdoor geeks, culture lovers & adventure seekers."- Add the text MEDIA KIT (remove "2017: )Thanks.Hendrik Added Thursday, January 5, 2017

Target Market(s)

The mediakit / brochure is for our partners (travel organisations, airline companies, PR companies and big brands like Pale Timber Co and Vesko).

And the readers of our website are independent travellers, outdoor geeks and adventure seekers. So the theme of the Mediakit must be 'travel inspiration'.

Industry/Entity Type

Travel Industry

Requirements
Must have
• • The media kit itself must be a travel experience / inspiration.
• • Colourful and clean design.
• • Use the colours of our new logo
• • Use our icons (marker, worldmap) in the design
• • Use the style of our website.
• • All the text in the media kit must be adjustable by us
• • Page format: A4
• • Number of pages: 6
• • It must be printable as a brochure (for presentations)
• • We also need a .pdf version of the brochure (for emailing it to our partners)

```html
<!DOCTYPE html>
<html lang="en">
<head>
<meta charset="utf-8">
<title>Bolderwijk – Stats</title>
<link href="https://fonts.googleapis.com/css2?family=Montserrat:wght@700;800;900&family=Open+Sans:wght@400;600;700&display=swap" rel="stylesheet">
<style>
  :root{
    --ink:#3b404c;
    --band:#3c4250;
    --lower:#50545e;
    --blue:#2aa7d9;
    --pink:#e8578b;
    --teal:#3aa0b3;
    --green:#7db544;
    --purple:#6c5ba6;
    --rose:#ee7fa6;
    --coral:#f08a65;
    --amber:#f6b93b;
    --gold:#e0a92a;
    --rule:#3b404c;
    --white:#ffffff;
    --paper:#ffffff;
  }
  *{box-sizing:border-box;margin:0;padding:0}
  html,body{width:848px;height:1200px;overflow:hidden;background:var(--paper)}
  body{font-family:"Open Sans",Arial,sans-serif;color:var(--ink)}
  .page{position:relative;width:848px;height:1200px;overflow:hidden;background:var(--paper)}
  .abs{position:absolute}

  /* header */
  .title-bar{left:100px;top:54px;width:691px;height:71px;background:var(--ink);clip-path:polygon(0 0,100% 0,97% 100%,0 100%)}
  .title-bar h1{position:absolute;left:36px;top:8px;font-family:"Montserrat",sans-serif;font-weight:900;font-size:40px;color:var(--white)}
  .brand-mark{left:40px;top:36px;width:60px;height:96px}
  .brand-mark .dot{position:absolute;left:4px;top:0;width:52px;height:52px;border-radius:50%;background:var(--ink)}
  .brand-mark .name{position:absolute;left:-8px;top:60px;width:76px;text-align:center;font-family:"Montserrat",sans-serif;font-weight:800;font-size:11px;color:var(--ink)}

  .section-title{font-family:"Montserrat",sans-serif;font-weight:900;font-size:26px;line-height:27px;text-align:center;color:var(--ink);text-transform:uppercase}
  .rule{background:var(--rule);height:2px}
  .label{font-family:"Montserrat",sans-serif;font-weight:800;font-size:17px;color:var(--ink)}

  /* gender */
  .gender svg{display:block}
  /* age bars */
  .age-row{position:absolute;left:240px;height:18px;display:flex;align-items:center}
  .age-row .bar{height:18px;display:flex;align-items:center;padding-left:5px;color:var(--white);font-size:11px;font-weight:700;white-space:nowrap}
  .age-row .pct{margin-left:5px;font-size:12px;font-weight:700;color:var(--ink)}
  .age-axis{left:221px;top:236px;width:2px;height:202px;background:var(--rule)}

  .map-area{left:64px;top:436px;width:186px;height:106px;border-radius:30px 40px 20px 36px;background:radial-gradient(ellipse at 50% 50%,#3b404c 0%,#2d313a 70%,rgba(45,49,58,0) 100%)}
  .map-pct{left:118px;top:470px;font-family:"Montserrat",sans-serif;font-weight:900;font-size:34px;color:var(--gold)}

  /* social */
  .social{position:absolute;left:553px;display:flex;align-items:center}
  .social .sq{width:44px;height:46px;background:var(--blue);border-radius:4px}
  .social .txt{margin-left:22px}
  .social .net{font-size:11px;font-weight:600;color:var(--ink);line-height:12px}
  .social .num{font-family:"Montserrat",sans-serif;font-weight:900;font-size:32px;line-height:34px;color:var(--ink)}
  .metric{left:553px;font-size:13px;color:var(--ink)}
  .metric-val{left:553px;font-family:"Montserrat",sans-serif;font-weight:700;font-size:22px;color:var(--pink)}

  /* work together band */
  .blue-line{left:0;top:582px;width:848px;height:3px;background:var(--blue)}
  .band{left:0;top:585px;width:848px;height:174px;background:var(--band)}
  .band h2{position:absolute;left:57px;top:36px;font-family:"Montserrat",sans-serif;font-weight:900;font-size:31px;line-height:33px;color:var(--white)}
  .band .mark{position:absolute;left:200px;top:58px;width:52px;height:52px;border-radius:50%;border:5px solid var(--blue)}
  .band .divider{position:absolute;left:278px;top:18px;width:2px;height:136px;background:#8a8f99}
  .band .pitch{position:absolute;left:309px;top:12px;width:500px;font-size:13.6px;line-height:18.6px;color:var(--white)}

  /* partners */
  .lower{left:0;top:759px;width:848px;height:441px;background:var(--lower)}
  .lower .globe{position:absolute;right:-80px;top:40px;width:420px;height:340px;border-radius:50%;background:radial-gradient(ellipse at center,rgba(240,138,101,.28),rgba(232,87,139,.12) 55%,rgba(80,84,94,0) 75%)}
  .partners-head{left:0;width:848px;text-align:center;font-family:"Montserrat",sans-serif;font-weight:800;font-size:24px;color:var(--blue)}
  .partners-copy{left:42px;width:770px;font-size:13.4px;line-height:17.5px;color:var(--white)}
  .strip{left:43px;width:776px;background:var(--white);display:flex;align-items:center;justify-content:space-around;padding:0 10px}
  .partner{display:flex;align-items:center;gap:6px;font-family:"Open Sans",sans-serif;font-weight:700;font-size:14px}
  .partner i{display:block;width:14px;height:14px}
</style>
</head>
<body>
<main class="page">

  <div class="abs brand-mark"><span class="dot"></span><span class="name">Bolderwijk</span></div>
  <header class="abs title-bar"><h1>Stats</h1></header>

  <!-- audience -->
  <h2 class="abs section-title" style="left:67px;top:153px;width:429px">Audience<br>Overview</h2>
  <div class="abs rule" style="left:67px;top:223px;width:429px"></div>
  <div class="abs" style="left:510px;top:150px;width:2px;height:306px;background:var(--rule)"></div>

  <div class="abs label" style="left:67px;top:248px">GENDER</div>
  <div class="abs gender" style="left:70px;top:275px">
    <svg width="140" height="110" viewBox="0 0 140 110">
      <circle cx="29" cy="34" r="25" fill="none" stroke="var(--rose)" stroke-width="6"/>
      <circle cx="29" cy="34" r="20" fill="var(--white)"/>
      <text x="29" y="40" text-anchor="middle" font-family="Montserrat,sans-serif" font-weight="800" font-size="16" fill="var(--pink)">66%</text>
      <line x1="29" y1="60" x2="29" y2="100" stroke="var(--rose)" stroke-width="6"/>
      <line x1="15" y1="82" x2="43" y2="82" stroke="var(--rose)" stroke-width="6"/>
      <circle cx="92" cy="36" r="25" fill="none" stroke="var(--teal)" stroke-width="6"/>
      <text x="92" y="42" text-anchor="middle" font-family="Montserrat,sans-serif" font-weight="800" font-size="16" fill="var(--teal)">34%</text>
      <line x1="110" y1="18" x2="128" y2="0" stroke="var(--teal)" stroke-width="6"/>
      <polygon points="112,-2 134,-2 134,20" fill="var(--teal)"/>
    </svg>
  </div>

  <div class="abs label" style="left:240px;top:248px">AGE</div>
  <div class="abs age-axis"></div>
  <div class="age-row" style="top:279px"><div class="bar" style="width:40px;background:var(--green)">18-24</div><span class="pct">11%</span></div>
  <div class="age-row" style="top:305px"><div class="bar" style="width:195px;background:var(--teal)">18-24</div><span class="pct">30%</span></div>
  <div class="age-row" style="top:331px"><div class="bar" style="width:231px;background:var(--purple)">18-24</div><span class="pct">36%</span></div>
  <div class="age-row" style="top:357px"><div class="bar" style="width:85px;background:var(--rose)">18-24</div><span class="pct">12%</span></div>
  <div class="age-row" style="top:383px"><div class="bar" style="width:54px;background:var(--coral)">18-24</div><span class="pct">9%</span></div>
  <div class="age-row" style="top:409px"><div class="bar" style="width:26px;background:var(--amber);padding-left:3px">65+</div><span class="pct">2%</span></div>
  <div class="abs rule" style="left:221px;top:458px;width:275px"></div>

  <div class="abs label" style="left:67px;top:407px">LOCATION</div>
  <div class="abs map-area" role="img" aria-label="World map showing reader locations"></div>
  <div class="abs map-pct">81%</div>

  <!-- traffic -->
  <h2 class="abs section-title" style="left:524px;top:153px;width:267px">Traffic &amp;<br>Social Media</h2>
  <div class="abs rule" style="left:524px;top:223px;width:267px"></div>

  <div class="social" style="top:245px"><span class="sq"></span><div class="txt"><div class="net">Friendwall</div><div class="num">30.000+</div></div></div>
  <div class="social" style="top:319px"><span class="sq"></span><div class="txt"><div class="net">Snapgrid</div><div class="num">5.200+</div></div></div>
  <div class="social" style="top:380px"><span class="sq"></span><div class="txt"><div class="net">Chirpline</div><div class="num">7000+</div></div></div>

  <div class="abs metric" style="top:447px">Number of unique visitors / month:</div>
  <div class="abs metric-val" style="top:466px">115.000</div>
  <div class="abs metric" style="top:510px">Number of page views / month:</div>
  <div class="abs metric-val" style="top:529px">240.000</div>

  <!-- work together -->
  <div class="abs blue-line"></div>
  <section class="abs band">
    <h2>Let’s<br>work<br>together!</h2>
    <span class="mark"></span>
    <span class="divider"></span>
    <p class="pitch">Wondering how to transform your product from a commodity into an experience?<br>
    Not sure how to leverage the power of social media and connect with your target demographic?<br>
    Need help aligning your branding with your company values?<br>
    Whether you are a tourism board, travel company, property, or product, we can help.<br>
    We work with more than 100 travel- and brand partners</p>
  </section>

  <!-- partners -->
  <section class="abs lower" role="img" aria-label="Faint world map decoration"><span class="globe"></span></section>

  <h2 class="abs partners-head" style="top:768px">Travel partners</h2>
  <p class="abs partners-copy" style="top:805px">We have worked with some of the world’s top travel companies &amp; destinations to help them achieve their goals. They leverage our authority and expertise in social media promotion, cross-marketing campaigns and unique content creation to showcase their offerings.</p>
  <div class="abs strip" style="top:873px;height:76px">
    <span class="partner" style="color:#1b8fd1"><i style="background:#1b8fd1;border-radius:50%"></i>Skylane Air</span>
    <span class="partner" style="color:#c0392b">Tuktu Travel</span>
    <span class="partner" style="color:#1c9bd7">Isla Sola</span>
    <span class="partner" style="color:#38a6d9">Farefinder</span>
    <span class="partner" style="color:#1b3f8f">Hazel Verre Reizen</span>
    <span class="partner" style="color:#1b3f8f">Meridian Airways</span>
  </div>

  <h2 class="abs partners-head" style="top:987px">Brand partners</h2>
  <p class="abs partners-copy" style="top:1025px">Bolderwijk reaches a niche audience of travellers passionate about unique experiences and amazing products. We have helped countless brands, from fashion labels to major technology corporations, bring their products to The Netherlands and reach their target consumers.</p>
  <div class="abs strip" style="top:1090px;height:110px">
    <span class="partner" style="color:#d0232a"><i style="background:#d0232a"></i>Pale Timber Co</span>
    <span class="partner" style="color:#222">Actacam</span>
    <span class="partner" style="color:#5a4a3a"><i style="border:2px solid #5a4a3a;border-radius:50%"></i>Kestrel Packs</span>
    <span class="partner" style="color:#222">Waypointer</span>
    <span class="partner" style="color:#222"><i style="background:#f7d117"></i>Vesko</span>
  </div>

</main>
</body>
</html>
```